3 glossy INFOGRAPHIC SPLASH PAGES for website of video production / photography studio website

Hello. We need 3 designed infographic images to act as 'splash pages' on our work-in-progress website to offer detailed information to visitors.
1. MUDMAP
2. RATECARD
3. STUDIO FLOORPLAN

To view the website WIP - Go here: http://www.sitevault.com.au/pelbrook/

Regarding FILE SIZES:

The MUDMAP should sit in landscape with dimensions 2048px wide x 1536px high.

The RATECARD and STUDIO FLOORPLAN should be laid out in PORTRAIT with dimensions 1526px wide x 2048px high.

Regarding DESIGNS:

First is a 'MUD MAP' that details travel and parking directions for visitors to our studio,

Second is a floorplan of our studio space, and

Third is a Studio Hire Rate Card.

We want these images to utilise our new theme / branding / logos (attached) and ultimately these designs need to be easily read and understood.

Attached Files (may not be in order in brief, but here is my list):

Target Market(s)

potential studio hire customers (mainly producers)

Industry/Entity Type

Film Production

Font styles to use
Sans Serif
Other font styles liked:
• I have supplied branding fonts to be used as you see fit.

Colors
fbed22
00a990
0292cd
fece3e
f78f20
f37122

Requirements
Must have
• Supplied logos and branding theme / colours (see attached).
• Predominantly gold colour (specific gold supplied) as well as utilising colour theme (see attached)
Nice to have
• Would be nice if all three images have a continuity in their layout / design

```html
<!DOCTYPE html>
<html lang="en">
<head>
<meta charset="utf-8">
<title>Pelbrook Studios – Parking Mud Map</title>
<link rel="stylesheet" href="https://fonts.googleapis.com/css2?family=Alfa+Slab+One&family=Lato:wght@400;700;900&display=swap">
<style>
  :root {
    --paper: #faf7ee;
    --gold: #c6a14b;
    --gold-deep: #a9832f;
    --gold-text: #c9a24a;
    --peach: #f5b48a;
    --peach-soft: #f9cc95;
    --label: #f0a46e;
    --line: #cfd8cf;
    --ink: #2e2413;
    --map: #e6e2da;
    --truck-orange: #f4a41f;
    --truck-grey: #a9b1b6;
    --truck-blue: #4aa8d8;
  }
  html, body { margin: 0; padding: 0; overflow: hidden; background: var(--paper); }
  .canvas { width: 1200px; height: 849px; position: relative; background: var(--paper); font-family: "Lato", sans-serif; }
  .canvas svg { display: block; }
  .title { font: 400 36px "Alfa Slab One", serif; fill: var(--ink); letter-spacing: 2.5px; }
  .subtitle { font: 700 11.5px "Lato", sans-serif; fill: var(--gold-text); }
  .street { font: 400 8.5px "Lato", sans-serif; fill: var(--label); letter-spacing: 2.5px; }
  .address { font: 700 12.5px "Lato", sans-serif; fill: var(--gold-text); letter-spacing: 3px; }
  .zone { font: 400 10.5px "Lato", sans-serif; fill: var(--label); letter-spacing: 2.5px; }
  .zone-small { font: 400 8px "Lato", sans-serif; fill: var(--label); letter-spacing: 1.5px; }
  .walkway { font: 400 10px "Lato", sans-serif; fill: var(--gold-text); writing-mode: vertical-rl; text-orientation: upright; letter-spacing: 2px; }
  .street-vertical { font: 400 8px "Lato", sans-serif; fill: var(--label); writing-mode: vertical-rl; text-orientation: upright; letter-spacing: 2px; }
  .brick-label { font: 400 9px "Lato", sans-serif; fill: var(--label); letter-spacing: 1px; }
  .badge-label { font: 700 8px "Lato", sans-serif; fill: var(--ink); }
  .badge-num { font: 900 17px "Lato", sans-serif; fill: var(--ink); }
  .route-note { font: 400 6.5px "Lato", sans-serif; fill: var(--ink); }
  .map-cta { font: 700 8px "Lato", sans-serif; fill: #fff; }
  .road { fill: none; stroke: var(--line); stroke-width: 1.2; }
  .arrow { fill: none; stroke: var(--gold); stroke-width: 1; stroke-linecap: round; stroke-linejoin: round; }
  .bay-gold { color: var(--gold); }
  .bay-peach { color: var(--peach); }
</style>
</head>
<body>
<div class="canvas">
<svg width="1200" height="849" viewBox="0 0 1200 849" xmlns="http://www.w3.org/2000/svg">
  <defs>
    <g id="arrow-right" class="arrow"><path d="M-5 0H5M2 -2.5L5 0 2 2.5"/></g>
    <g id="parking-bay">
      <circle r="16" fill="none" stroke="currentColor" stroke-width="3"/>
      <path d="M-11 3V0Q-10 -2.5 -6 -2.5L-3 -5.5Q0 -6.5 4 -5.5L7.5 -2.5Q11 -2.5 11.5 0.5V3Z" fill="currentColor"/>
      <path d="M-3 -2.5L-1.5 -4.5H3.5L5.5 -2.5Z" fill="var(--paper)"/>
      <path d="M-11 4H11.5" stroke="currentColor" stroke-width="1"/>
    </g>
    <g id="truck-body">
      <rect x="0" y="0" width="33" height="20" rx="1.5"/>
      <path d="M35 6H43L49 13V22H35Z"/>
    </g>
  </defs>

  <!-- header -->
  <text class="title" x="600" y="80" text-anchor="middle">— PELBROOK STUDIOS —</text>
  <text class="subtitle" x="600" y="109" text-anchor="middle">PELBROOK STUDIOS ESSENTIAL &amp; NON ESSENTIAL</text>
  <text class="subtitle" x="600" y="123" text-anchor="middle">VEHICLE PARKING VIA HARROW ST.</text>

  <!-- roads -->
  <path class="road" d="M258 139V197H894V139"/>
  <text class="street" x="600" y="181" text-anchor="middle">HARROW ST</text>
  <path class="road" d="M205 147V538"/>
  <path class="road" d="M978 139V742H1167"/>
  <path class="road" d="M255 607H896V790H1167"/>
  <text class="street" x="573" y="633" text-anchor="middle">UNRESTRICTED STREET PARKING</text>
  <text class="street-vertical" x="172" y="322">LINDEN ST</text>

  <!-- lots -->
  <rect class="road" x="258" y="253" width="297" height="306"/>
  <path class="road" d="M287 253V442H555"/>
  <rect class="road" x="641" y="253" width="254" height="306"/>

  <!-- sub-station -->
  <g fill="var(--peach)">
    <rect x="483" y="258" width="14" height="7" rx="1"/><rect x="499" y="258" width="14" height="7" rx="1"/><rect x="515" y="258" width="14" height="7" rx="1"/>
    <rect x="483" y="268" width="6" height="7" rx="1"/><rect x="491" y="268" width="14" height="7" rx="1"/><rect x="507" y="268" width="14" height="7" rx="1"/><rect x="523" y="268" width="6" height="7" rx="1"/>
    <rect x="483" y="278" width="14" height="7" rx="1"/><rect x="499" y="278" width="14" height="7" rx="1"/><rect x="515" y="278" width="14" height="7" rx="1"/>
    <rect x="483" y="288" width="6" height="7" rx="1"/><rect x="491" y="288" width="14" height="7" rx="1"/><rect x="507" y="288" width="14" height="7" rx="1"/><rect x="523" y="288" width="6" height="7" rx="1"/>
    <rect x="483" y="298" width="14" height="7" rx="1"/><rect x="499" y="298" width="14" height="7" rx="1"/><rect x="515" y="298" width="14" height="7" rx="1"/>
  </g>
  <text class="brick-label" transform="translate(467 260) rotate(90)">BRICK</text>
  <text class="zone" x="504" y="318" text-anchor="middle">SUB-STATION</text>

  <!-- essential parking -->
  <text class="zone" x="540" y="385" text-anchor="end">ESSENTIAL PARKING</text>
  <text class="zone-small" x="428" y="415" text-anchor="end">ROLLER DOOR/ REAR</text>
  <text class="zone-small" x="428" y="424" text-anchor="end">STAGE DOOR ACCESS</text>
  <g transform="translate(433 405)">
    <use href="#truck-body" fill="var(--truck-orange)"/>
    <path d="M38 8H42.5L46 12.5H38Z" fill="#fff"/>
    <circle cx="9" cy="23" r="4" fill="#2e2e2e"/><circle cx="9" cy="23" r="1.6" fill="#fff"/>
    <circle cx="42" cy="23" r="4" fill="#2e2e2e"/><circle cx="42" cy="23" r="1.6" fill="#fff"/>
  </g>
  <g transform="translate(495 405) scale(-1 1) translate(-49 0)">
    <rect x="0" y="0" width="33" height="20" rx="1.5" fill="var(--truck-grey)"/>
    <path d="M35 6H43L49 13V22H35Z" fill="var(--truck-blue)"/>
    <path d="M38 8H42.5L46 12.5H38Z" fill="#fff"/>
    <circle cx="9" cy="23" r="4" fill="#2e2e2e"/><circle cx="9" cy="23" r="1.6" fill="#fff"/>
    <circle cx="42" cy="23" r="4" fill="#2e2e2e"/><circle cx="42" cy="23" r="1.6" fill="#fff"/>
  </g>
  <path class="arrow" d="M465 433l4 7 4-7 4 7 4-7 4 7 4-7"/>

  <!-- studio building -->
  <rect x="385" y="443" width="168" height="116" fill="var(--gold)" role="img" aria-label="Studio building illustration"/>
  <circle cx="371" cy="503" r="27" fill="var(--gold)" stroke="#fff" stroke-width="3"/>
  <path class="arrow" d="M455 561l4 7 4-7 4 7 4-7 4 7 4-7"/>
  <text class="address" x="554" y="588" text-anchor="middle">PELBROOK STUDIOS - 42B MARLOW ST</text>

  <!-- walkway -->
  <text class="walkway" x="597" y="318">PEDESTRIAN WALKWAY</text>

  <!-- non-essential parking bays -->
  <g role="img" aria-label="Non-essential parking bays">
    <use href="#parking-bay" class="bay-gold" x="697" y="293"/><use href="#parking-bay" class="bay-peach" x="764" y="293"/><use href="#parking-bay" class="bay-peach" x="832" y="293"/>
    <use href="#parking-bay" class="bay-gold" x="697" y="343"/><use href="#parking-bay" class="bay-gold" x="764" y="343"/><use href="#parking-bay" class="bay-peach" x="832" y="343"/>
    <use href="#parking-bay" class="bay-gold" x="697" y="393"/><use href="#parking-bay" class="bay-peach" x="764" y="393"/><use href="#parking-bay" class="bay-peach" x="832" y="393"/>
    <use href="#parking-bay" class="bay-gold" x="697" y="443"/><use href="#parking-bay" class="bay-gold" x="764" y="443"/><use href="#parking-bay" class="bay-peach" x="832" y="443"/>
  </g>
  <text class="zone-small" x="770" y="490" text-anchor="middle">NON - ESSENTIAL</text>
  <text class="zone-small" x="770" y="500" text-anchor="middle">PARKING</text>

  <!-- roundabout -->
  <circle cx="206" cy="593" r="31" fill="var(--gold)"/>
  <circle cx="206" cy="593" r="28" fill="none" stroke="var(--gold-deep)" stroke-dasharray="2 2"/>

  <!-- traffic arrows -->
  <g class="arrow">
    <path d="M191 546q5 2 9-1M214 544q6-2 9-6"/>
    <path d="M233 235q1-5 8-6M570 229q7 1 7 7M580 316q-3 4-7 4M625 316q0 4-6 5M626 236q0-6 6-7M918 227q7-2 10 4"/>
  </g>
  <use href="#arrow-right" x="261" y="227"/><use href="#arrow-right" x="306" y="227"/><use href="#arrow-right" x="346" y="227"/><use href="#arrow-right" x="387" y="227"/>
  <use href="#arrow-right" x="428" y="227"/><use href="#arrow-right" x="469" y="227"/><use href="#arrow-right" x="509" y="227"/><use href="#arrow-right" x="550" y="227"/>
  <g transform="translate(577 0)"><use href="#arrow-right" transform="translate(0 248) rotate(90)"/><use href="#arrow-right" transform="translate(0 273) rotate(90)"/><use href="#arrow-right" transform="translate(0 298) rotate(90)"/></g>
  <g transform="translate(625 0)"><use href="#arrow-right" transform="translate(0 248) rotate(90)"/><use href="#arrow-right" transform="translate(0 273) rotate(90)"/><use href="#arrow-right" transform="translate(0 298) rotate(90)"/></g>
  <g transform="translate(0 227)">
    <use href="#arrow-right" transform="translate(650 0) rotate(180)"/><use href="#arrow-right" transform="translate(691 0) rotate(180)"/><use href="#arrow-right" transform="translate(732 0) rotate(180)"/>
    <use href="#arrow-right" transform="translate(771 0) rotate(180)"/><use href="#arrow-right" transform="translate(812 0) rotate(180)"/><use href="#arrow-right" transform="translate(852 0) rotate(180)"/><use href="#arrow-right" transform="translate(892 0) rotate(180)"/>
  </g>
  <g transform="translate(936 0)">
    <use href="#arrow-right" transform="translate(0 240) rotate(-90)"/><use href="#arrow-right" transform="translate(0 270) rotate(-90)"/><use href="#arrow-right" transform="translate(0 311) rotate(-90)"/><use href="#arrow-right" transform="translate(0 351) rotate(-90)"/>
    <use href="#arrow-right" transform="translate(0 392) rotate(-90)"/><use href="#arrow-right" transform="translate(0 432) rotate(-90)"/><use href="#arrow-right" transform="translate(0 472) rotate(-90)"/><use href="#arrow-right" transform="translate(0 513) rotate(-90)"/>
    <use href="#arrow-right" transform="translate(0 553) rotate(-90)"/><use href="#arrow-right" transform="translate(0 594) rotate(-90)"/><use href="#arrow-right" transform="translate(0 635) rotate(-90)"/><use href="#arrow-right" transform="translate(0 675) rotate(-90)"/>
    <use href="#arrow-right" transform="translate(0 716) rotate(-90)"/><use href="#arrow-right" transform="translate(0 748) rotate(-90)"/>
  </g>
  <g transform="translate(231 0)">
    <use href="#arrow-right" transform="translate(0 261) rotate(-90)"/><use href="#arrow-right" transform="translate(0 303) rotate(-90)"/><use href="#arrow-right" transform="translate(0 347) rotate(-90)"/>
    <use href="#arrow-right" transform="translate(0 388) rotate(-90)"/><use href="#arrow-right" transform="translate(0 434) rotate(-90)"/><use href="#arrow-right" transform="translate(0 475) rotate(-90)"/><use href="#arrow-right" transform="translate(0 520) rotate(-90)"/>
  </g>
  <g transform="translate(0 767)">
    <use href="#arrow-right" transform="translate(982 0) rotate(180)"/><use href="#arrow-right" transform="translate(1023 0) rotate(180)"/><use href="#arrow-right" transform="translate(1063 0) rotate(180)"/>
    <use href="#arrow-right" transform="translate(1104 0) rotate(180)"/><use href="#arrow-right" transform="translate(1144 0) rotate(180)"/>
  </g>

  <!-- route 1 -->
  <rect x="77" y="51" width="70" height="63" fill="var(--gold)" role="img" aria-label="City skyline icon"/>
  <path d="M57 118H180V110L197 132 180 154V146H57Z" fill="var(--peach-soft)"/>
  <path d="M32 132l10-16h19l10 16-10 16H42Z" fill="var(--peach-soft)" stroke="var(--paper)" stroke-width="2"/>
  <path d="M36 132l8-13h15l8 13-8 13H44Z" fill="var(--peach-soft)" stroke="var(--gold)" stroke-width="1"/>
  <text class="badge-num" x="51" y="138" text-anchor="middle">1</text>
  <text class="badge-label" x="107" y="135" text-anchor="middle">FERNCLIFF RD</text>
  <text class="route-note" x="110" y="155" text-anchor="middle">PELBROOK STUDIOS VIA CITY/</text>
  <text class="route-note" x="110" y="163" text-anchor="middle">FERNCLIFF RD - 6 KMS / 10 MINS</text>

  <!-- route 2 -->
  <rect x="1047" y="607" width="86" height="45" fill="var(--gold)" role="img" aria-label="Bridge icon"/>
  <path d="M1149 658H1025V650L1004 674 1025 698V690H1149Z" fill="var(--peach-soft)"/>
  <path d="M1140 674l10-16h19l10 16-10 16h-19Z" fill="var(--peach-soft)" stroke="var(--paper)" stroke-width="2"/>
  <path d="M1144 674l8-13h15l8 13-8 13h-15Z" fill="var(--peach-soft)" stroke="var(--gold)" stroke-width="1"/>
  <text class="badge-num" x="1160" y="680" text-anchor="middle">2</text>
  <text class="badge-label" x="1090" y="677" text-anchor="middle">EASTVALE BRIDGE</text>
  <text class="route-note" x="1094" y="699" text-anchor="middle">PELBROOK STUDIOS VIA</text>
  <text class="route-note" x="1094" y="707" text-anchor="middle">EASTVALE BRIDGE - 5 MINS</text>

  <!-- map strip -->
  <rect x="27" y="717" width="456" height="105" fill="var(--peach)"/>
  <rect x="77" y="720" width="403" height="99" fill="var(--map)" role="img" aria-label="Street map of the neighbourhood around the studio"/>
  <circle cx="68" cy="771" r="26" fill="var(--peach)" stroke="#fff" stroke-width="2"/>
  <text class="map-cta" x="68" y="765" text-anchor="middle">Check</text>
  <text class="map-cta" x="68" y="774" text-anchor="middle">Online</text>
  <text class="map-cta" x="68" y="783" text-anchor="middle">Map</text>
</svg>
</div>
</body>
</html>
```